National Intensive Course Provider needs an advert designed to appear in trams

We need an advertisement designed to put in trams, the dimensions are 660mm wide and 203mm height. We offer intensive driving courses all over the UK, allowing pupils to complete a full driving course within a week/two weeks with both the theory and practical tests included in the course (as required). We would like the colours used to be green and dark blue, maybe red also, whatever looks best from them colours really.

Key Points to highlight:
- Pass your driving test within 1 week
- Start your course as early as next week
- Both tests included as part of your course (if required)

I have attached some images which could be included in the design

```html
<!DOCTYPE html>
<html lang="en">
<head>
<meta charset="utf-8">
<title>Fastlane Driving – Tram Advert</title>
<link rel="stylesheet" href="https://fonts.googleapis.com/css2?family=Exo+2:ital,wght@1,700;1,800&display=swap">
<style>
  :root {
    --page-bg: #dfe0e2;
    --navy: #131640;
    --navy-deep: #0d0f2e;
    --navy-light: #1e2260;
    --green: #9acd32;
    --red: #e2202a;
    --white: #ffffff;
    --photo-a: #5a6470;
    --photo-b: #2a2f38;
    --photo-c: #9aa3a8;
  }
  * { margin: 0; padding: 0; box-sizing: border-box; }
  html, body { width: 1200px; height: 472px; overflow: hidden; background: var(--page-bg); }
  .advert {
    position: absolute; left: 42px; top: 64px;
    width: 1116px; height: 342px;
    font-family: "Exo 2", Arial, sans-serif;
    font-style: italic;
  }
  .advert-art { position: absolute; inset: 0; width: 100%; height: 100%; display: block; }
  .benefit {
    position: absolute; color: var(--white);
    font-weight: 800; font-size: 21px; line-height: 26px;
    letter-spacing: 0.3px; text-transform: uppercase; white-space: nowrap;
  }
  .benefit-mark { position: absolute; width: 14px; height: 16px; }
  .benefit--speed { left: 595px; top: 50px; }
  .mark--speed { left: 570px; top: 56px; }
  .benefit--start { left: 537px; top: 126px; }
  .mark--start { left: 512px; top: 132px; }
  .benefit--tests { left: 482px; top: 196px; }
  .mark--tests { left: 456px; top: 202px; }
  .contact-phone {
    position: absolute; left: 367px; top: 301px;
    display: flex; align-items: center; gap: 6px;
    color: var(--navy); font-weight: 800; font-size: 27px; letter-spacing: 0.5px;
  }
  .contact-phone svg { width: 20px; height: 20px; }
  .contact-web {
    position: absolute; left: 638px; top: 310px;
    color: var(--navy); font-weight: 800; font-size: 13.5px; letter-spacing: 0.2px;
  }
  .brand-badge {
    position: absolute; left: 970px; top: 234px; width: 124px; height: 92px;
    background: var(--navy); border: 2px solid var(--red); border-radius: 14px;
    display: flex; align-items: center; justify-content: center; text-align: center;
  }
  .brand-name {
    color: var(--white); font-weight: 800; font-size: 17px; line-height: 20px;
    text-transform: uppercase;
  }
</style>
</head>
<body>
  <div class="advert">
    <svg class="advert-art" viewBox="53 80 1394 427" preserveAspectRatio="none" aria-hidden="false">
      <defs>
        <linearGradient id="panelFill" x1="0" y1="0" x2="1" y2="1">
          <stop offset="0" stop-color="var(--navy-light)"/>
          <stop offset="0.5" stop-color="var(--navy)"/>
          <stop offset="1" stop-color="var(--navy-deep)"/>
        </linearGradient>
        <linearGradient id="photoFill" x1="0" y1="0" x2="1" y2="0.6">
          <stop offset="0" stop-color="var(--photo-b)"/>
          <stop offset="0.55" stop-color="var(--photo-a)"/>
          <stop offset="1" stop-color="var(--photo-c)"/>
        </linearGradient>
      </defs>
      <rect class="panel" x="53" y="80" width="1394" height="427" fill="url(#panelFill)"/>
      <g role="img" aria-label="Photo: young driver in a checked shirt holding the steering wheel of a moving car">
        <polygon points="53,80 636,80 482,507 53,507" fill="url(#photoFill)"/>
      </g>
      <polygon class="stripe-green" points="632,80 659,80 506,507 479,507" fill="var(--green)"/>
      <polygon class="stripe-green-short" points="665,80 688,80 611,272 593,272" fill="var(--green)"/>
      <polygon class="contact-band" points="497,441 1210,441 1255,347 1447,347 1447,507 475,507" fill="var(--white)"/>
      <polyline class="contact-rule" points="497,441 1210,441 1255,347 1447,347" fill="none" stroke="var(--red)" stroke-width="4"/>
    </svg>

    <svg class="benefit-mark mark--speed" viewBox="0 0 14 16"><polygon points="0,0 14,8 0,16 4,8" fill="var(--green)"/></svg>
    <p class="benefit benefit--speed">Pass your driving test within 1 week</p>

    <svg class="benefit-mark mark--start" viewBox="0 0 14 16"><polygon points="0,0 14,8 0,16 4,8" fill="var(--green)"/></svg>
    <p class="benefit benefit--start">Start your course as early as next week</p>

    <svg class="benefit-mark mark--tests" viewBox="0 0 14 16"><polygon points="0,0 14,8 0,16 4,8" fill="var(--green)"/></svg>
    <p class="benefit benefit--tests">Both tests included as part of<br>your course (if required)</p>

    <p class="contact-phone">
      <svg viewBox="0 0 24 24"><path fill="var(--red)" d="M6.6 10.8c1.4 2.8 3.8 5.1 6.6 6.6l2.2-2.2c.3-.3.7-.4 1-.2 1.1.4 2.3.6 3.6.6.6 0 1 .4 1 1V20c0 .6-.4 1-1 1C10.6 21 3 13.4 3 4c0-.6.4-1 1-1h3.5c.6 0 1 .4 1 1 0 1.3.2 2.5.6 3.6.1.3 0 .7-.2 1L6.6 10.8z"/></svg>
      0200 555 0142
    </p>
    <p class="contact-web">WWW.FASTLANEDRIVINGWEEK.COM</p>

    <div class="brand-badge">
      <span class="brand-name">Fastlane<br>Driving</span>
    </div>
  </div>
</body>
</html>
```